Luxury Business Card Design

We need a business card design for a law firm that look sophisticated and luxury

Target Market(s)

Australian legal markets

Industry/Entity Type

Legal

Contact Information for Business Card

Attached

Requirements
Must have
• Logo, head office address on front side and 2 other addresses on the back side.
Nice to have
• Please see below our current business card. Need something more sophisticated and luxury feel

```html
<!DOCTYPE html>
<html lang="en">
<head>
<meta charset="utf-8">
<title>Ashcombe Lawyers – Business Cards</title>
<link rel="stylesheet" href="https://fonts.googleapis.com/css2?family=EB+Garamond:wght@400;500;600&display=swap">
<style>
  :root {
    --bg: #e8e4dd;
    --paper: #ffffff;
    --ink: #15241a;
    --forest: #0a1a10;
    --forest-soft: #0f2216;
    --gold: #c49a45;
    --text-light: #f2efe8;
    --muted: #3a3a3a;
  }
  * { box-sizing: border-box; margin: 0; padding: 0; }
  html, body { width: 1200px; height: 900px; overflow: hidden; }
  body {
    background: var(--bg);
    font-family: "EB Garamond", Georgia, serif;
    position: relative;
  }
  .card {
    position: absolute;
    width: 620px;
    height: 360px;
    border-radius: 30px;
    box-shadow: 0 10px 30px rgba(0,0,0,.18);
    overflow: hidden;
  }
  .card--front { left: 90px; top: 70px; background: var(--paper); color: var(--muted); }
  .card--back { left: 490px; top: 470px; background: var(--forest); color: var(--text-light); }

  /* Front card */
  .tagline {
    position: absolute; left: 38px; top: 36px;
    font-size: 17px; font-weight: 600; letter-spacing: .5px; color: var(--ink);
  }
  .offices { position: absolute; left: 38px; top: 78px; list-style: none; width: 360px; }
  .office { font-size: 14.5px; line-height: 1.25; margin-bottom: 14px; }
  .office__city { color: var(--gold); text-transform: uppercase; }

  .brand {
    position: absolute; display: flex; flex-direction: column; align-items: center;
  }
  .brand__mark { border-radius: 50%; border: 4px solid var(--gold); }
  .brand__name {
    margin-top: 14px; font-weight: 500; text-transform: uppercase;
    letter-spacing: 3px; text-align: center; line-height: 1.1;
  }
  .card--front .brand { right: 36px; top: 110px; }
  .card--front .brand__mark { width: 86px; height: 86px; }
  .card--front .brand__name { color: var(--ink); font-size: 30px; }

  /* Back card */
  .person { position: absolute; left: 34px; top: 150px; }
  .person__name { color: var(--gold); font-size: 21px; text-transform: uppercase; letter-spacing: .5px; }
  .person__role { font-size: 15px; line-height: 1.25; }

  .decor-ring {
    position: absolute; left: 110px; top: 225px; width: 125px; height: 125px;
    border-radius: 50%; border: 8px solid var(--forest-soft);
  }

  .contacts { position: absolute; right: 30px; top: 34px; list-style: none; width: 280px; }
  .contact { display: flex; align-items: center; gap: 9px; font-size: 14px; line-height: 1.35; }
  .contact svg { width: 12px; height: 12px; flex: none; fill: none; stroke: var(--gold); stroke-width: 1.6; }
  .contact--address { align-items: flex-start; }
  .contact--address svg { margin-top: 3px; }

  .divider { position: absolute; right: 30px; top: 176px; width: 290px; height: 1px; background: var(--gold); }

  .card--back .brand { right: 34px; top: 196px; flex-direction: row; gap: 18px; }
  .card--back .brand__mark { width: 78px; height: 78px; }
  .card--back .brand__name { margin-top: 0; color: var(--text-light); font-size: 28px; text-align: left; }
</style>
</head>
<body>

<section class="card card--front" aria-label="Business card front">
  <p class="tagline">YOUR COUNSEL. YOUR FUTURE. IT COUNTS</p>
  <ul class="offices">
    <li class="office"><span class="office__city">Melbourne Office -</span> Suite 310, Ashford Chambers<br>212 Little Lonsdale Street, Melbourne, VIC, 3000<br>P: (03) 9000 2417</li>
    <li class="office"><span class="office__city">Sydney -</span> Level 9, Harbourview Building, 18 Station Street<br>PARRAMATTA, NSW 2150<br>P: +61 02 8000 3391</li>
    <li class="office"><span class="office__city">Perth Office -</span> Unit 4, 17 Lakeside Drive<br>Joondalup, WA, 6027<br>P: 0400 261 734</li>
  </ul>
  <div class="brand">
    <div class="brand__mark"></div>
    <p class="brand__name">Ashcombe<br>Lawyers</p>
  </div>
</section>

<section class="card card--back" aria-label="Business card back">
  <div class="decor-ring"></div>
  <div class="person">
    <p class="person__name">Rohan Mehra</p>
    <p class="person__role">Director and Principal Solicitor<br>MBA, Juris Doctor</p>
  </div>
  <ul class="contacts">
    <li class="contact"><svg viewBox="0 0 12 12"><rect x="3" y="1" width="6" height="10" rx="1"/></svg>+61 7 3000 4812</li>
    <li class="contact"><svg viewBox="0 0 12 12"><path d="M2 2c0 5 3 8 8 8l1-2-2-1-1 1C6 7 5 6 4 4l1-1-1-2z"/></svg>+61 0400 261 734</li>
    <li class="contact"><svg viewBox="0 0 12 12"><rect x="1" y="2.5" width="10" height="7"/><path d="M1 2.5l5 4 5-4"/></svg>rohan@ashcombelawyers.com.au</li>
    <li class="contact"><svg viewBox="0 0 12 12"><circle cx="6" cy="6" r="5"/><path d="M1 6h10M6 1c-2 3-2 7 0 10M6 1c2 3 2 7 0 10"/></svg>www.ashcombelawyers.com.au</li>
    <li class="contact contact--address"><svg viewBox="0 0 12 12"><path d="M6 11S2 7 2 4.5a4 4 0 018 0C10 7 6 11 6 11z"/><circle cx="6" cy="4.5" r="1.3"/></svg>Level 2/48 Harbour Terrace<br>Spring Hill QLD 4000, Australia</li>
  </ul>
  <div class="divider"></div>
  <div class="brand">
    <div class="brand__mark"></div>
    <p class="brand__name">Ashcombe<br>Lawyers</p>
  </div>
</section>

</body>
</html>
```